Website Design for two swimming school brands

Looking for a modern, engaging website design for my new business Every Stroke Water Learning. Within that business I have two current brands:
Every Stroke Swim and Yard Paddle
My current website (www.yardpaddle.net) has most of the info you'll need. Feel free to also use my socials for content.
Looking for someone to do the initial design/setup and then hand over full control to me with no ongoing fees or charges (except for hosting), and I'm responsible for all future changes. Ideally made and then can be edited in google sites but open to other options.

Website requirements are quite simple for both pages.
For the Yard Paddle page, I'd like the same info and features that are on my current website presented in a fresh way.
For the Every Stroke page, I'd like to see your concepts for design and possible sections, but it'll be roughly the same as the yard paddle one. I will upload a document soon for text and sections and other information to go on the Every stroke swim page.

For clarity the difference between the business' is one goes out to people's home pools and the other hires out lane space in public pool to conduct lessons.
I'd like a lighter theme for the Yard Paddle Website and a Darker one for the Every Stroke.
Both pages needs to be accessible with picture descriptions for screen reader and other similar features.

I currently use Bookora for all my inquiry, booking and payment functions so the website would need to be compatible with their widgets.

Have a look at the MockUp v2 or the business card design to get the concept of two different brandings working together.

Some text from the Every Stroke Swim Page can be found in this document:
https://docs.example-files.net/document/d/7QpaLmRvXc2TnWb8KdYs4FgHe9JuZoNi3VcXaBt/edit?usp=sharing
-
Feel free to ask any further questions.
Updates

Target Market(s)

Families and disability service providers

Industry/Entity Type

Sports and Recreation

Coding

Coded - Design and coding required

Number of Pages Required

4 page

Requirements
Must have
• Engaging design, ability to put in widgets into website, cross links between two business
Nice to have
• Common elements across the two pages but also points of difference

```html
<!DOCTYPE html>
<html lang="en">
<head>
<meta charset="utf-8">
<title>Yard Paddle – Mobile Swimming Lessons</title>
<link rel="stylesheet" href="https://fonts.googleapis.com/css2?family=Lexend:wght@300;400;500;600;700&family=Mulish:wght@400;600;700&display=swap">
<style>
:root{
  --navy:#112c37;
  --navy-deep:#0c232d;
  --teal:#17947f;
  --teal-bright:#1fc1a1;
  --forest:#0d6656;
  --blue:#1e8fd0;
  --sky:#dff3f5;
  --ink:#1b2a30;
  --muted:#5d6a70;
  --white:#ffffff;
  --head:"Lexend",sans-serif;
  --body:"Mulish",sans-serif;
}
*{box-sizing:border-box;margin:0;padding:0}
html,body{width:1200px;height:4405px;overflow:hidden;background:var(--white)}
body{font-family:var(--body);color:var(--ink)}
.page{position:relative;width:1200px;height:4405px;overflow:hidden}
.abs{position:absolute}
ul{list-style:none}

/* header / hero */
.hero-band{left:0;top:0;width:1200px;height:680px}
.brand{left:70px;top:40px;display:flex;align-items:center;gap:8px;font-family:var(--head);font-weight:500;font-size:20px;color:var(--teal-bright);letter-spacing:.5px}
.brand .mark{width:12px;height:12px;background:var(--teal-bright);border-radius:50%}
.topmail{right:72px;top:8px;font-size:11px;color:#cfe0e6;display:flex;align-items:center;gap:5px}
.nav{left:497px;top:0;display:flex;height:70px}
.nav a{font-family:var(--head);font-size:12.5px;color:#e6eef1;text-decoration:none;padding:45px 0 0;margin-right:47px;letter-spacing:.3px}
.nav a.active{background:var(--blue);padding:45px 11px 0;color:#fff;margin-right:38px;height:70px}
.nav a:last-child{margin-right:0}
.hero-photo{left:72px;top:84px;width:1056px;height:477px;background:linear-gradient(120deg,#2a9fd8 0%,#56c1ea 45%,#1b7fbf 100%)}
.hero-title{left:761px;top:182px;font-family:var(--head);color:#fff}
.hero-title .l1{font-size:42px;font-weight:600;line-height:46px;letter-spacing:.5px}
.hero-title .l2{font-size:55px;font-weight:700;line-height:60px;margin-top:4px;letter-spacing:0}
.hero-sub{left:761px;top:360px;font-family:var(--head);font-size:18px;color:#fff;font-weight:300}
.btn-light{left:761px;top:415px;width:128px;height:40px;background:#fff;color:var(--navy);font-family:var(--head);font-size:11px;font-weight:600;display:flex;align-items:center;justify-content:center;letter-spacing:.3px}
.dots{left:26px;top:303px}
.dots span{display:block;width:6px;height:6px;border-radius:50%;background:#fff;margin:0 auto 18px}
.dots span.on{width:16px;height:16px;border:2px solid var(--teal-bright);background:transparent;position:relative}
.dots span.on::after{content:"";position:absolute;left:3px;top:3px;width:6px;height:6px;border-radius:50%;background:var(--teal-bright)}
.free{left:0;top:585px;width:1200px;text-align:center;font-family:var(--head);font-size:18px;color:#fff;font-weight:300}
.free b{color:var(--teal-bright);font-weight:500}
.free .star{color:#f5c518}

/* welcome */
.welcome-kicker{left:72px;top:844px;font-family:var(--head);font-size:21px;font-weight:300}
.welcome-title{left:72px;top:872px;font-family:var(--head);font-size:36px;font-weight:400}
.welcome-text{left:72px;top:934px;width:490px;font-size:13.4px;line-height:22px;color:#333}
.btn-teal{background:var(--teal);color:#fff;font-family:var(--head);font-size:11.5px;font-weight:500;display:flex;align-items:center;justify-content:center;letter-spacing:.3px}
.welcome-btn{left:72px;top:1073px;width:128px;height:40px}
.welcome-photo{left:653px;top:752px;width:462px;height:462px;border-radius:50%;background:radial-gradient(circle at 45% 40%,#cfe8ef 0%,#7cc4de 45%,#3a8fb8 100%)}

/* classes */
.classes-kicker{left:0;top:1290px;width:1200px;text-align:center;font-family:var(--head);font-size:21px;font-weight:300}
.classes-title{left:0;top:1316px;width:1200px;text-align:center;font-family:var(--head);font-size:36px;font-weight:400}
.sky-band{left:0;top:1620px;width:1200px;height:340px}
.card{top:1450px;width:337px;height:246px;background:#fff;border-radius:10px;box-shadow:0 3px 14px rgba(0,0,0,.12);border-bottom:3px solid var(--teal);text-align:center}
.card .avatar{position:absolute;left:103px;top:-63px;width:130px;height:130px;border-radius:50%;border:3px solid #fff;box-shadow:0 0 0 2px var(--teal)}
.card h3{margin-top:88px;font-family:var(--head);font-weight:400;font-size:17.5px}
.card p{margin:14px 24px 0;font-size:12px;line-height:20px;color:var(--muted);height:60px}
.card hr{border:0;border-top:1px solid #e5e9ea;margin:6px 24px 0}
.card .more{margin-top:14px;font-family:var(--head);font-size:11px;color:var(--teal);font-weight:500}

/* about */
.about-title{left:0;top:1748px;width:1200px;text-align:center;font-family:var(--head);font-size:36px;font-weight:400}
.about-text{left:60px;top:1814px;width:1080px;text-align:center;font-size:13.4px;line-height:22px;color:#2d3a3f}
.about-btn{left:535px;top:1900px;width:130px;height:40px}
.about-photo{left:0;top:1950px;width:1200px;height:404px;background:linear-gradient(180deg,#bfe8f4 0%,#56b9e6 35%,#1f8fd0 100%)}

/* grid */
.tile{width:352px;height:275px}
.tile-text{width:352px;height:275px;padding:38px 12px 0 36px}
.tile-text.left{padding-left:0}
.tile-text h3{font-family:var(--head);font-weight:300;font-size:26px;line-height:33px}
.tile-text ul{margin-top:18px}
.tile-text li{font-size:12px;color:#333;margin-bottom:16px;white-space:nowrap}
.tile-text li::before{content:"";display:inline-block;width:4px;height:4px;background:var(--teal-bright);margin-right:5px;vertical-align:middle}

/* testimonials */
.testi-title{left:0;top:3048px;width:1200px;text-align:center;font-family:var(--head);font-size:36px;font-weight:400}
.testi-box{left:162px;top:3145px;width:795px;height:290px}
.testi-name{left:204px;top:3198px;font-family:var(--head);font-size:26px;font-weight:300}
.testi-text{left:206px;top:3244px;width:500px;font-size:13.4px;line-height:22px;color:#333}
.testi-sign{left:392px;top:3466px;font-family:var(--head);font-size:17px;font-weight:300}
.testi-photo{left:745px;top:3142px;width:392px;height:353px;border-radius:46% 46% 40% 40%/40% 40% 30% 30%;background:radial-gradient(ellipse at 50% 45%,#b7d6e8 0%,#e9eef1 55%,#ffffff 72%)}
.arrow{width:48px;height:48px;border-radius:50%;background:#fff;box-shadow:0 2px 8px rgba(0,0,0,.15);display:flex;align-items:center;justify-content:center}
.hatch{left:0;top:3513px;width:1200px;height:39px;background:repeating-linear-gradient(135deg,#d4e8e3 0 2px,#f4faf8 2px 7px)}

/* contact */
.contact{left:0;top:3552px;width:1200px;height:500px;background:var(--navy)}
.contact-title{left:0;top:3616px;width:1200px;text-align:center;font-family:var(--head);font-size:36px;color:#fff;font-weight:400}
.contact-sub{left:0;top:3664px;width:1200px;text-align:center;font-size:13px;color:#d7e3e7}
.field{background:#fff;width:375px;height:43px;font-size:11px;padding:13px 14px;color:#333}
.field.msg{height:96px}
.submit{left:603px;top:3806px;width:375px;height:43px;font-family:var(--head);font-size:12.5px}

/* footer */
.footer{left:0;top:3920px;width:1200px;height:485px}
.foot-brand{left:70px;top:4158px;display:flex;align-items:center;gap:10px;font-family:var(--head);font-size:32px;font-weight:500;color:#fff}
.foot-brand .mark{width:16px;height:16px;border:2px solid #fff}
.foot-note{left:70px;top:4203px;font-size:11px;color:#d6ebe6}
.social{top:4230px;width:32px;height:32px;border-radius:50%;background:#0a4d41}
.foot-col h4{font-family:var(--head);font-size:18px;font-weight:400;color:var(--teal-bright);margin-bottom:20px}
.foot-col li{font-size:12px;color:#e4f1ee;margin-bottom:15px;display:flex;align-items:center;gap:9px}
.foot-col li::before{content:"";width:6px;height:6px;border-radius:50%;background:#fff}
.foot-col.contacts li::before{display:none}
.foot-col.contacts li{align-items:flex-start;margin-bottom:22px;line-height:15px}
.ico{flex:0 0 30px;width:30px;height:30px;border-radius:50%;border:1.5px solid #fff;display:flex;align-items:center;justify-content:center}
.divider{top:4074px;width:0;height:170px;border-left:1px dashed rgba(255,255,255,.35)}
.copy{left:0;top:4346px;width:1200px;text-align:center;font-size:11px;color:#e4f1ee}
.copy span{color:var(--teal-bright)}
</style>
</head>
<body>
<div class="page">

  <!-- Header & hero -->
  <svg class="abs hero-band" viewBox="0 0 1200 680" aria-hidden="true">
    <path d="M0 0H1200V600C1000 700 800 560 560 620C360 670 160 690 0 640Z" fill="var(--navy)"/>
  </svg>
  <div class="abs brand"><span class="mark"></span>YARD PADDLE</div>
  <div class="abs topmail">
    <svg width="12" height="9" viewBox="0 0 12 9"><rect width="12" height="9" fill="#fff"/><path d="M0 0L6 5L12 0" stroke="#112c37" fill="none"/></svg>
    eastside@yardpaddle.net
  </div>
  <nav class="abs nav">
    <a class="active">HOME</a><a>ABOUT US</a><a>MY SERVICES</a><a>TESTIMONIALS</a><a>PRICING</a><a>LINKS</a>
  </nav>
  <div class="abs hero-photo" role="img" aria-label="Instructor and smiling children splashing together in a bright blue pool"></div>
  <div class="abs hero-title"><div class="l1">MOBILE</div><div class="l2">SWIMMING<br>LESSONS</div></div>
  <div class="abs hero-sub">For all Ages and Abilities in Adelaide</div>
  <div class="abs btn-light">EXPLORE MORE</div>
  <div class="abs dots"><span class="on"></span><span></span><span></span></div>
  <div class="abs free"><span class="star">★</span>&nbsp; <b>FREE</b> in-Home Pool and Swimmer Assessment</div>

  <!-- Welcome -->
  <div class="abs welcome-kicker">Welcome To</div>
  <h1 class="abs welcome-title">Yard Paddle</h1>
  <p class="abs welcome-text">With over 10 years' experience teaching children, teenagers and adults, Tom brings the skills, knowledge, and passion to help swimmers of all ages and abilities achieve their goals. Yard Paddle offers a personalised approach to swimming lessons that can help individuals overcome their fears and technical challenges...</p>
  <div class="abs btn-teal welcome-btn">READ MORE</div>
  <div class="abs welcome-photo" role="img" aria-label="Instructor teaching a young boy in goggles at the edge of an indoor pool"></div>

  <!-- Classes -->
  <svg class="abs sky-band" viewBox="0 0 1200 340" aria-hidden="true">
    <path d="M0 30C300 -10 700 60 1200 20V340H0Z" fill="var(--sky)"/>
  </svg>
  <div class="abs classes-kicker">Private Lessons and Group</div>
  <h2 class="abs classes-title">Classes are Availiable For:</h2>

  <div class="abs card" style="left:72px">
    <div class="avatar" role="img" aria-label="Smiling child in a green swim cap" style="background:radial-gradient(circle,#9fd58a,#2d9fcc)"></div>
    <h3>Children and Teenagers</h3>
    <p>Helping every child no matter their age** reach their full potential</p>
    <hr><div class="more">READ MORE</div>
  </div>
  <div class="abs card" style="left:431px">
    <div class="avatar" role="img" aria-label="Adult swimmer in a pink cap smiling in open water" style="background:radial-gradient(circle,#3e9fd8,#1d5f8a)"></div>
    <h3>Adults</h3>
    <p>Helping adults learn, whether for the first time or now that they want to try it out again</p>
    <hr><div class="more">READ MORE</div>
  </div>
  <div class="abs card" style="left:791px">
    <div class="avatar" role="img" aria-label="Instructor giving a high five to a swimmer at the pool edge" style="background:radial-gradient(circle,#cfe3ee,#4a87b4)"></div>
    <h3>People with a Disability</h3>
    <p>Enabling children and adults to overcome the challenges their disability presents, helping them achieve their goals</p>
    <hr><div class="more">READ MORE</div>
  </div>

  <!-- About -->
  <h2 class="abs about-title">About Me</h2>
  <p class="abs about-text">Tom’s life, from the very start, revolved around water. His parents met in a swimming club and started him swimming before he could walk!<br>From a young age, teaching has come naturally to him and it is something that he truly enjoys. In his spare time, he enjoys hiking with friends and playing Ultimate Frisbee, including helping to coordinate a weekly social league.</p>
  <div class="abs btn-teal about-btn">READ MORE</div>
  <div class="abs about-photo" role="img" aria-label="Three happy children in swim caps and goggles swimming towards the camera"></div>

  <!-- Grid -->
  <div class="abs tile" style="left:72px;top:2432px;background:linear-gradient(160deg,#6fc3e4,#2f86b6)" role="img" aria-label="Instructor high fiving a swimmer at a pool with kickboards on the deck"></div>
  <div class="abs tile" style="left:424px;top:2432px;background:linear-gradient(180deg,#e8eef0 0%,#9dd6e6 45%,#1aa9d1 100%)" role="img" aria-label="Bright indoor lap pool with a tiled deck"></div>
  <div class="abs tile-text" style="left:776px;top:2432px">
    <h3>Why Tom and Yard Paddle Swim?</h3>
    <ul>
      <li>Experienced, Qualified and Police Cleared</li>
      <li>Individual Approach</li>
      <li>Focus on both Technique and Water Safety</li>
      <li>Free home pool and swimmer assessment</li>
    </ul>
  </div>
  <div class="abs tile-text left" style="left:72px;top:2706px">
    <h3 style="margin-top:36px">What You Can Expect</h3>
    <ul>
      <li>Clear and prompt communication</li>
      <li>Balance between stucture and having fun</li>
      <li>Fast skill acquisition and progression too new skills</li>
    </ul>
  </div>
  <div class="abs tile" style="left:424px;top:2706px;background:linear-gradient(160deg,#3fb2d8,#1b86b4)" role="img" aria-label="Older woman smiling while holding a kickboard in the pool"></div>
  <div class="abs tile" style="left:776px;top:2706px;background:linear-gradient(160deg,#2aa3e0,#1a7cc4)" role="img" aria-label="Adult swimmer doing freestyle in a lap lane"></div>

  <!-- Testimonials -->
  <h2 class="abs testi-title">Testimonials</h2>
  <svg class="abs testi-box" viewBox="0 0 795 290" aria-hidden="true">
    <path d="M35 1H795" fill="none" stroke="var(--teal)" stroke-width="2"/>
    <path d="M1 30V282H230L285 305L290 282H795" fill="none" stroke="var(--teal)" stroke-width="2"/>
    <path d="M9 2V22M-1 12H19" stroke="var(--blue)" stroke-width="3"/>
  </svg>
  <div class="abs testi-name">Family of Six</div>
  <p class="abs testi-text">Tom was always a friendly, welcoming and knowledgeable person at the swim school we attended for our children. He was only too happy to assist my family and I with requests/questions and the children loved having him as a teacher. They said Tom made learning to swim fun and certainly this was reflected in their progress. I have no hesitation in recommending Tom as a swimming instructor to you and your family.</p>
  <div class="abs testi-sign">Mark &amp; Ellie</div>
  <div class="abs testi-photo" role="img" aria-label="Smiling couple sitting together on the floor"></div>
  <div class="abs arrow" style="left:60px;top:3277px"><svg width="12" height="12" viewBox="0 0 12 12"><path d="M8 1L3 6L8 11" stroke="#222" stroke-width="2" fill="none"/></svg></div>
  <div class="abs arrow" style="left:1090px;top:3277px"><svg width="12" height="12" viewBox="0 0 12 12"><path d="M4 1L9 6L4 11" stroke="#222" stroke-width="2" fill="none"/></svg></div>
  <div class="abs hatch"></div>

  <!-- Contact -->
  <div class="abs contact"></div>
  <h2 class="abs contact-title">Contact Us</h2>
  <div class="abs contact-sub">I'll work with you to find a time and day that is suitable</div>
  <div class="abs field" style="left:220px;top:3701px">Name:</div>
  <div class="abs field" style="left:220px;top:3754px">Email:</div>
  <div class="abs field" style="left:220px;top:3806px">Phone:</div>
  <div class="abs field msg" style="left:603px;top:3701px">Message:</div>
  <div class="abs btn-teal submit">SUBMIT</div>

  <!-- Footer -->
  <svg class="abs footer" viewBox="0 0 1200 485" aria-hidden="true">
    <path d="M0 100C200 40 420 40 590 75C700 95 760 110 840 100C980 85 1100 50 1200 18V485H0Z" fill="var(--forest)"/>
    <path d="M0 95C200 35 420 35 590 70C700 90 760 105 840 95C980 80 1100 45 1200 13" fill="none" stroke="#fff" stroke-width="5"/>
  </svg>
  <div class="abs foot-brand"><span class="mark"></span>YARD PADDLE</div>
  <div class="abs foot-note">Use the 'live site' icons on the right or email me</div>
  <div class="abs social" style="left:74px" aria-label="Social profile one"></div>
  <div class="abs social" style="left:119px" aria-label="Social profile two"></div>

  <div class="abs foot-col" style="left:431px;top:4066px">
    <h4>Sitemap</h4>
    <ul><li>Home</li><li>About Me</li><li>My Services</li><li>Testimonials</li><li>Links</li><li>Contact Us</li></ul>
  </div>
  <div class="abs divider" style="left:580px"></div>
  <div class="abs foot-col" style="left:627px;top:4066px">
    <h4>Services</h4>
    <ul><li>Children and Teenagers</li><li>Adults</li><li>People with a Disability</li></ul>
  </div>
  <div class="abs divider" style="left:840px"></div>
  <div class="abs foot-col contacts" style="left:880px;top:4066px">
    <h4>Contacts</h4>
    <ul>
      <li><span class="ico"><svg width="12" height="15" viewBox="0 0 12 15"><path d="M6 14C6 14 1 8.5 1 5.5A5 5 0 0 1 11 5.5C11 8.5 6 14 6 14Z" fill="#fff"/><circle cx="6" cy="5.5" r="2" fill="#0d6656"/></svg></span>Northgate, SA, Australia Eastwood,<br>Riverbend, Oakvale, SA, Australia</li>
      <li style="align-items:center"><span class="ico"><svg width="14" height="14" viewBox="0 0 14 14"><path d="M3 1L5.5 4L4 6C5 8 6 9 8 10L10 8.5L13 11L11.5 13C6 13 1 8 1 2.5Z" fill="#fff"/></svg></span>+2 (555) 240 7300</li>
      <li style="align-items:center"><span class="ico"><svg width="14" height="10" viewBox="0 0 14 10"><rect width="14" height="10" rx="1" fill="#fff"/><path d="M0 0L7 6L14 0" stroke="#0d6656" fill="none"/></svg></span>eastside@yardpaddle.net</li>
    </ul>
  </div>
  <div class="abs copy">Copyright © 2022 <span>Yard Paddle</span>. All Rights Reserved.</div>

</div>
</body>
</html>
```